Wordpress Corporate Website for New Business

We need a corporate website created which will act as a professional shop window for our new business. We do not need special features like merchant facilities or chatbots. The attachment shows suggested key sections as well as some possible wording. Various versions of the company logo have been attached as well to give different options to play with. We are looking for an option which is easy for us to take over and manage moving forward should we need to make minor updates.

Target Market(s)

Corporate entities

Industry/Entity Type

Private share auctions

Coding

Coded - Design and coding required

```html
<!DOCTYPE html>
<html lang="en">
<head>
<meta charset="utf-8">
<title>TradeCrest – Private Share Auctions</title>
<link href="https://fonts.googleapis.com/css2?family=Montserrat:wght@500;600;700;800&family=Roboto:wght@400;500&display=swap" rel="stylesheet">
<style>
:root{
  --purple:#8a0b8f;
  --purple-dark:#6a0a7a;
  --navy:#0f0b8c;
  --navy-deep:#0a0870;
  --ink:#1d1d2b;
  --grey-text:#555566;
  --faq-bg:#f3f3f5;
  --footer-bg:#f6f6f8;
  --white:#ffffff;
}
*{margin:0;padding:0;box-sizing:border-box}
html,body{width:1200px;height:4412px;overflow:hidden}
body{position:relative;background:var(--white);font-family:"Montserrat",sans-serif;color:var(--ink)}
.abs{position:absolute}

/* nav */
.site-nav{position:absolute;left:0;top:0;width:1200px;height:79px;background:var(--white)}
.brand{position:absolute;left:60px;top:22px;display:flex;align-items:center;gap:10px;font-weight:700;font-size:31px;line-height:36px;color:var(--purple)}
.brand-dot{width:28px;height:28px;border-radius:50%;background:var(--navy)}
.menu{position:absolute;right:80px;top:37px;display:flex;gap:27px;font-size:14.5px;font-weight:600;color:var(--navy);white-space:nowrap}
.menu .active{color:var(--purple)}

/* hero */
.hero{position:absolute;left:0;top:79px;width:1200px;height:549px;overflow:hidden;
  background:linear-gradient(100deg,var(--navy) 0%,#3a0b9a 45%,#7a0b8c 100%);
  border-bottom-right-radius:290px 210px}
.hero h1{position:absolute;left:127px;top:180px;font-size:44px;line-height:51px;font-weight:700;color:var(--white)}
.hero-photo{position:absolute;left:690px;top:30px;width:330px;height:519px;border-radius:160px 160px 0 0;
  background:linear-gradient(180deg,#e9b94a 0%,#f0b323 50%,#d99a14 100%);opacity:.9}

/* headings */
.section-title{position:absolute;left:0;width:1200px;text-align:center;font-size:40px;font-weight:700;line-height:46px}
.section-title .p{color:var(--purple)}
.section-title .n{color:var(--navy)}

.about-text{position:absolute;left:220px;top:756px;width:760px;text-align:center;font-size:16.5px;line-height:24px;font-weight:500;color:#333}
.divider{position:absolute;left:127px;top:897px;width:946px;height:1px;background:#cfcfd6}

/* pricing */
.plan{position:absolute;border:2px solid var(--purple);border-radius:12px;background:var(--white);overflow:hidden;text-align:center}
.plan-head{background:var(--purple);color:var(--white);padding-top:26px}
.plan-head .tier{font-size:18px;font-weight:700}
.plan-head .price{font-size:32px;font-weight:700;margin-top:6px}
.plan-head .price sup{font-size:16px;vertical-align:14px}
.plan-head .price small{font-size:13px;font-weight:500}
.plan ul{list-style:none;text-align:left;margin:30px 0 0 36px}
.plan li{font-size:15px;line-height:29px;color:#333;font-weight:500;display:flex;align-items:center;gap:8px}
.plan li svg{flex:none}
.plan .btn{display:inline-block;margin-top:24px;width:144px;height:41px;line-height:41px;border-radius:21px;background:var(--purple);color:var(--white);font-size:15px;font-weight:700}
.plan.featured{border-color:var(--navy)}
.plan.featured .plan-head{background:var(--navy)}
.plan.featured .btn{background:var(--navy)}

/* key features */
.features-band{position:absolute;left:0;top:1555px;width:1200px;height:465px;
  background:linear-gradient(90deg,#160c94 0%,#3d0c99 45%,#7c0c90 100%)}
.features-band h2{position:absolute;left:0;top:110px;width:1200px;text-align:center;color:var(--white);font-size:40px;font-weight:700}
.features-band p{position:absolute;left:250px;top:170px;width:700px;text-align:center;color:var(--white);font-size:16.5px;line-height:24px;font-weight:500}
.pill{position:absolute;top:282px;height:55px;border-radius:28px;border:2px solid var(--white);color:var(--white);font-size:20px;font-weight:700;text-align:center;line-height:51px}
.pill.company{left:402px;width:194px;background:var(--purple)}
.pill.holder{left:604px;width:194px;background:var(--navy)}

/* why choose */
.why-item{position:absolute;width:340px;font-family:"Roboto",sans-serif}
.why-item h3{font-family:"Montserrat",sans-serif;font-size:20px;font-weight:700;color:var(--ink);margin-bottom:6px}
.why-item p{font-size:13.5px;line-height:18px;color:var(--grey-text)}
.why-item.right{text-align:right}
.node{position:absolute;width:110px;height:110px;border-radius:50%;background:var(--white);border:2px solid var(--purple);display:flex;align-items:center;justify-content:center}
.node span{width:92px;height:92px;border-radius:50%;background:var(--purple);display:flex;align-items:center;justify-content:center}
.node.navy{border-color:var(--navy)}
.node.navy span{background:var(--navy)}
.hub-name{position:absolute;left:499px;top:2406px;width:200px;text-align:center;font-size:30px;font-weight:700;color:var(--purple)}

/* contact */
.contact-band{position:absolute;left:0;top:2893px;width:1200px;height:428px;
  background:radial-gradient(ellipse at 50% 100%,#2b22c8 0%,#130ea0 45%,var(--navy-deep) 100%)}
.contact-frame{position:absolute;left:291px;top:118px;width:618px;height:208px;border:1px solid rgba(255,255,255,.7);border-top:none}
.frame-top{position:absolute;top:118px;height:1px;background:rgba(255,255,255,.7)}
.contact-band h2{position:absolute;left:500px;top:96px;width:200px;text-align:center;font-size:40px;font-weight:700;color:var(--white)}
.contact-line{position:absolute;top:190px;display:flex;align-items:center;gap:10px;color:var(--white);font-size:19px;font-weight:700;line-height:22px}
.contact-line .ic{width:42px;height:42px;border-radius:50%;border:2px solid var(--white);display:flex;align-items:center;justify-content:center}
.connect-btn{position:absolute;left:488px;top:272px;width:226px;height:55px;border-radius:28px;border:2px solid var(--purple);background:var(--navy);color:var(--white);font-size:20px;font-weight:700;text-align:center;line-height:51px}

/* support */
.support-text{position:absolute;left:0;top:3447px;width:1200px;text-align:center;font-family:"Roboto",sans-serif;font-size:15.5px;line-height:20px;color:#222}
.support-text u{color:var(--navy)}
.faq{position:absolute;left:288px;width:624px;height:51px;background:var(--faq-bg);border-radius:4px;display:flex;align-items:center;justify-content:space-between;padding:0 20px 0 22px;font-size:16.5px;font-weight:600;color:var(--ink)}

/* footer */
.footer{position:absolute;left:0;top:3912px;width:1200px;height:500px;background:var(--footer-bg)}
.footer-band{position:absolute;left:0;top:0;width:1200px;height:120px;background:linear-gradient(90deg,var(--navy) 0%,#4a0c9a 50%,var(--purple) 100%)}
.footer-brand{position:absolute;left:0;top:210px;width:1200px;display:flex;justify-content:center;align-items:center;gap:16px;font-size:66px;font-weight:700;color:var(--navy)}
.footer-brand i{width:56px;height:56px;border-radius:50%;background:var(--purple);display:block}
.footer-menu{position:absolute;left:0;top:307px;width:1200px;display:flex;justify-content:center;gap:30px;font-size:16px;font-weight:600;color:#333}
.copyright{position:absolute;left:0;top:362px;width:1200px;text-align:center;font-family:"Roboto",sans-serif;font-size:15px;color:#444}
.social{position:absolute;left:558px;top:404px;width:66px;height:66px;border-radius:50%;background:linear-gradient(135deg,var(--navy),var(--purple))}
.contact-us{position:absolute;left:1007px;top:402px;width:161px;height:48px;border-radius:24px;background:var(--navy);color:var(--white);font-size:19px;font-weight:700;text-align:center;line-height:48px}
</style>
</head>
<body>

<header class="site-nav">
  <div class="brand"><span class="brand-dot"></span>TradeCrest</div>
  <nav class="menu">
    <span class="active">Home</span><span>About</span><span>Pricing</span><span>Key Features</span><span>Why Choose TradeCrest</span><span>Contact</span><span>Support</span><span>FAQ</span>
  </nav>
</header>

<section class="hero">
  <h1>Retain Control,<br>Unlock Liquidity</h1>
  <div class="hero-photo" role="img" aria-label="Photo of a smiling woman in a yellow top holding a smartphone"></div>
</section>

<h2 class="section-title" style="top:693px"><span class="p">About</span> <span class="n">TradeCrest</span></h2>
<p class="about-text">At TradeCrest, we empower private companies to take control of their share transactions without the hassle of third-party involvement. Our innovative share exchange platform is designed to connect pre-approved buyers and sellers directly, fostering a secure and efficient environment for trading ownership in private enterprises.</p>
<div class="divider"></div>

<h2 class="section-title" style="top:943px"><span class="p">Pricing</span> <span class="n">Plans</span></h2>

<div class="plan" style="left:127px;top:1048px;width:292px;height:411px">
  <div class="plan-head" style="height:113px"><div class="tier">TIER 1</div><div class="price"><sup>$</sup>0.00<small>/month</small></div></div>
  <ul>
    <li><svg width="14" height="14" viewBox="0 0 14 14"><circle cx="7" cy="7" r="6" fill="none" stroke="#8a0b8f" stroke-width="1.4"/><path d="M4 7.2l2 2 4-4" fill="none" stroke="#8a0b8f" stroke-width="1.4"/></svg>Lorem ipsum dolor sit</li>
    <li><svg width="14" height="14" viewBox="0 0 14 14"><circle cx="7" cy="7" r="6" fill="none" stroke="#8a0b8f" stroke-width="1.4"/><path d="M4 7.2l2 2 4-4" fill="none" stroke="#8a0b8f" stroke-width="1.4"/></svg>Consectetur adipiscinlit</li>
    <li><svg width="14" height="14" viewBox="0 0 14 14"><circle cx="7" cy="7" r="6" fill="none" stroke="#8a0b8f" stroke-width="1.4"/><path d="M4 7.2l2 2 4-4" fill="none" stroke="#8a0b8f" stroke-width="1.4"/></svg>Sed do eiusmod tempor</li>
    <li><svg width="14" height="14" viewBox="0 0 14 14"><circle cx="7" cy="7" r="6" fill="none" stroke="#8a0b8f" stroke-width="1.4"/><path d="M4 7.2l2 2 4-4" fill="none" stroke="#8a0b8f" stroke-width="1.4"/></svg>Qcididunt ut labortdolore</li>
    <li><svg width="14" height="14" viewBox="0 0 14 14"><circle cx="7" cy="7" r="6" fill="none" stroke="#8a0b8f" stroke-width="1.4"/><path d="M4 7.2l2 2 4-4" fill="none" stroke="#8a0b8f" stroke-width="1.4"/></svg>Magna aliquauis ipsum</li>
    <li><svg width="14" height="14" viewBox="0 0 14 14"><circle cx="7" cy="7" r="6" fill="none" stroke="#8a0b8f" stroke-width="1.4"/><path d="M4 7.2l2 2 4-4" fill="none" stroke="#8a0b8f" stroke-width="1.4"/></svg>Suspendisse ultrices</li>
  </ul>
  <span class="btn">Get Started</span>
</div>

<div class="plan featured" style="left:442px;top:1029px;width:316px;height:449px">
  <div class="plan-head" style="height:139px;padding-top:32px"><div class="tier">TIER 2</div><div class="price"><sup>$</sup>29.00<small>/month</small></div></div>
  <ul style="margin-left:50px">
    <li><svg width="14" height="14" viewBox="0 0 14 14"><circle cx="7" cy="7" r="6" fill="none" stroke="#0f0b8c" stroke-width="1.4"/><path d="M4 7.2l2 2 4-4" fill="none" stroke="#0f0b8c" stroke-width="1.4"/></svg>Lorem ipsum dolor sit</li>
    <li><svg width="14" height="14" viewBox="0 0 14 14"><circle cx="7" cy="7" r="6" fill="none" stroke="#0f0b8c" stroke-width="1.4"/><path d="M4 7.2l2 2 4-4" fill="none" stroke="#0f0b8c" stroke-width="1.4"/></svg>Consectetur adipiscinlit</li>
    <li><svg width="14" height="14" viewBox="0 0 14 14"><circle cx="7" cy="7" r="6" fill="none" stroke="#0f0b8c" stroke-width="1.4"/><path d="M4 7.2l2 2 4-4" fill="none" stroke="#0f0b8c" stroke-width="1.4"/></svg>Sed do eiusmod tempor</li>
    <li><svg width="14" height="14" viewBox="0 0 14 14"><circle cx="7" cy="7" r="6" fill="none" stroke="#0f0b8c" stroke-width="1.4"/><path d="M4 7.2l2 2 4-4" fill="none" stroke="#0f0b8c" stroke-width="1.4"/></svg>Qcididunt ut labortdolore</li>
    <li><svg width="14" height="14" viewBox="0 0 14 14"><circle cx="7" cy="7" r="6" fill="none" stroke="#0f0b8c" stroke-width="1.4"/><path d="M4 7.2l2 2 4-4" fill="none" stroke="#0f0b8c" stroke-width="1.4"/></svg>Magna aliquauis ipsum</li>
    <li><svg width="14" height="14" viewBox="0 0 14 14"><circle cx="7" cy="7" r="6" fill="none" stroke="#0f0b8c" stroke-width="1.4"/><path d="M4 7.2l2 2 4-4" fill="none" stroke="#0f0b8c" stroke-width="1.4"/></svg>Suspendisse ultrices</li>
  </ul>
  <span class="btn">Get Started</span>
</div>

<div class="plan" style="left:779px;top:1048px;width:292px;height:411px">
  <div class="plan-head" style="height:113px"><div class="tier">TIER 3</div><div class="price"><sup>$</sup>49.00<small>/month</small></div></div>
  <ul>
    <li><svg width="14" height="14" viewBox="0 0 14 14"><circle cx="7" cy="7" r="6" fill="none" stroke="#8a0b8f" stroke-width="1.4"/><path d="M4 7.2l2 2 4-4" fill="none" stroke="#8a0b8f" stroke-width="1.4"/></svg>Lorem ipsum dolor sit</li>
    <li><svg width="14" height="14" viewBox="0 0 14 14"><circle cx="7" cy="7" r="6" fill="none" stroke="#8a0b8f" stroke-width="1.4"/><path d="M4 7.2l2 2 4-4" fill="none" stroke="#8a0b8f" stroke-width="1.4"/></svg>Consectetur adipiscinlit</li>
    <li><svg width="14" height="14" viewBox="0 0 14 14"><circle cx="7" cy="7" r="6" fill="none" stroke="#8a0b8f" stroke-width="1.4"/><path d="M4 7.2l2 2 4-4" fill="none" stroke="#8a0b8f" stroke-width="1.4"/></svg>Sed do eiusmod tempor</li>
    <li><svg width="14" height="14" viewBox="0 0 14 14"><circle cx="7" cy="7" r="6" fill="none" stroke="#8a0b8f" stroke-width="1.4"/><path d="M4 7.2l2 2 4-4" fill="none" stroke="#8a0b8f" stroke-width="1.4"/></svg>Qcididunt ut labortdolore</li>
    <li><svg width="14" height="14" viewBox="0 0 14 14"><circle cx="7" cy="7" r="6" fill="none" stroke="#8a0b8f" stroke-width="1.4"/><path d="M4 7.2l2 2 4-4" fill="none" stroke="#8a0b8f" stroke-width="1.4"/></svg>Magna aliquauis ipsum</li>
    <li><svg width="14" height="14" viewBox="0 0 14 14"><circle cx="7" cy="7" r="6" fill="none" stroke="#8a0b8f" stroke-width="1.4"/><path d="M4 7.2l2 2 4-4" fill="none" stroke="#8a0b8f" stroke-width="1.4"/></svg>Suspendisse ultrices</li>
  </ul>
  <span class="btn">Get Started</span>
</div>

<section class="features-band" role="img" aria-label="Background photo of a city skyline with a blue to purple tint">
  <h2>Key Features</h2>
  <p>Lorem ipsum dolor sit amet, consectetur adipiscing elit, sed do eiusmod tempor incididunt ut labore et dolore magna aliqua. Quis ipsum suspendisse ultrices gravida. Risus commodo viverra maecenas accumsan lacus vel facilisis.</p>
  <div class="pill company">Company</div>
  <div class="pill holder">Shareholder</div>
</section>

<h2 class="section-title" style="top:2100px"><span class="p">Why Choose</span><br><span class="n">TradeCrest</span></h2>

<svg class="abs" style="left:0;top:0" width="1200" height="4412" viewBox="0 0 1200 4412" aria-hidden="true">
  <circle cx="599" cy="2440" r="200" fill="none" stroke="#8a0b8f" stroke-width="2.5"/>
</svg>

<div class="hub-name">TradeCrest</div>

<div class="node" style="left:448px;top:2225px"><span>
  <svg width="44" height="44" viewBox="0 0 44 44" fill="none" stroke="#fff" stroke-width="2.2"><path d="M22 6a14 14 0 0 1 14 14v6M8 26v-6a14 14 0 0 1 6-11.5"/><path d="M22 12a8 8 0 0 1 8 8v8M14 28v-8a8 8 0 0 1 4-7"/><path d="M22 18v14"/></svg></span></div>
<div class="node" style="left:655px;top:2225px"><span>
  <svg width="44" height="44" viewBox="0 0 44 44" fill="none" stroke="#fff" stroke-width="2.2"><rect x="8" y="12" width="28" height="22" rx="2"/><path d="M22 16l7 3v5c0 4-3 7-7 8-4-1-7-4-7-8v-5z"/></svg></span></div>
<div class="node navy" style="left:368px;top:2369px"><span>
  <svg width="44" height="44" viewBox="0 0 44 44" fill="none" stroke="#fff" stroke-width="2.2"><rect x="10" y="20" width="22" height="16" rx="2"/><path d="M15 20v-5a6 6 0 0 1 12 0v5"/><circle cx="21" cy="28" r="2"/><path d="M36 16l4-2M36 22h4M36 28l4 2"/></svg></span></div>
<div class="node navy" style="left:727px;top:2369px"><span>
  <svg width="44" height="44" viewBox="0 0 44 44" fill="none" stroke="#fff" stroke-width="2.2"><circle cx="22" cy="22" r="15"/><ellipse cx="22" cy="22" rx="7" ry="15"/><path d="M7 22h30M10 14h24M10 30h24"/></svg></span></div>
<div class="node" style="left:407px;top:2518px"><span>
  <svg width="44" height="44" viewBox="0 0 44 44" fill="none" stroke="#fff" stroke-width="2.2"><path d="M8 18h24l-5-5M36 26H12l5 5"/><circle cx="22" cy="22" r="6"/></svg></span></div>
<div class="node" style="left:688px;top:2513px"><span>
  <svg width="44" height="44" viewBox="0 0 44 44" fill="none" stroke="#fff" stroke-width="2.2"><rect x="8" y="22" width="14" height="14"/><path d="M22 8h14v14" stroke-dasharray="3 3"/><path d="M26 18l10-10M30 8h6v6"/></svg></span></div>
<div class="node navy" style="left:544px;top:2578px"><span>
  <svg width="44" height="44" viewBox="0 0 44 44" fill="none" stroke="#fff" stroke-width="2.2"><circle cx="26" cy="16" r="10"/><path d="M26 10v12M29 12h-4a2 2 0 0 0 0 4h2a2 2 0 0 1 0 4h-4"/><path d="M6 36h8v-10H6zM14 28l8-2h6"/></svg></span></div>

<div class="why-item right" style="left:76px;top:2203px"><h3>Retain Control</h3><p>Companies can maintain control over who participates in their auctions. This control is essential for preserving the company's culture, protecting sensitive information, and ensuring that only pre-approved parties are involved.</p></div>
<div class="why-item" style="left:794px;top:2201px;width:310px"><h3>Secure and Confidential</h3><p>We understand the importance of privacy. Our security measures safeguard your sensitive information, providing a secure space for seamless share trading.</p></div>
<div class="why-item right" style="left:64px;top:2381px;width:290px"><h3>Unlock Liquidity</h3><p>TradeCrest provides a structured marketplace which facilitates efficient and easy share transactions, creating a level of liquidity not previously experienced by private company investors.</p></div>
<div class="why-item" style="left:851px;top:2367px;width:290px"><h3>Global Reach</h3><p>Our platform allows companies and investors from around the world to connect and engage in share auctions effortlessly, no matter where they are located.</p></div>
<div class="why-item right" style="left:72px;top:2553px;width:310px"><h3>Direct Transactions</h3><p>Say goodbye to intermediaries. Our platform enables shareholders in private companies to trade shares directly, ensuring transparency and efficiency in every transaction.</p></div>
<div class="why-item" style="left:818px;top:2533px;width:290px"><h3>Scalability</h3><p>The TradeCrest platform can scale to accommodate the needs of companies of varying sizes, from startups to well-established enterprises.</p></div>
<div class="why-item" style="left:414px;top:2704px;width:370px;text-align:center"><h3>Price Discovery</h3><p>Private share auctions help establish fair market values for shares, as the auction process allows market forces to determine the price. This can be especially valuable for shareholders who are looking to assess the value of their holdings.</p></div>

<section class="contact-band" role="img" aria-label="Blue background with a faint hexagon network pattern">
  <div class="contact-frame"></div>
  <div class="frame-top" style="left:291px;width:212px"></div>
  <div class="frame-top" style="left:700px;width:209px"></div>
  <h2>Contact</h2>
  <div class="contact-line" style="left:352px">
    <span class="ic"><svg width="20" height="20" viewBox="0 0 24 24" fill="#fff"><path d="M6.6 10.8a15 15 0 0 0 6.6 6.6l2.2-2.2a1 1 0 0 1 1-.25 11.4 11.4 0 0 0 3.6.57 1 1 0 0 1 1 1V20a1 1 0 0 1-1 1A17 17 0 0 1 3 4a1 1 0 0 1 1-1h3.5a1 1 0 0 1 1 1c0 1.25.2 2.45.57 3.57a1 1 0 0 1-.25 1z"/></svg></span>
    <span>Phone number:<br>+65 9000 4821</span>
  </div>
  <div class="contact-line" style="left:599px">
    <span class="ic"><svg width="20" height="20" viewBox="0 0 24 24" fill="#fff"><path d="M3 5h18a1 1 0 0 1 1 1v12a1 1 0 0 1-1 1H3a1 1 0 0 1-1-1V6a1 1 0 0 1 1-1zm1 2v.4l8 5 8-5V7l-8 5z"/></svg></span>
    <span>Email:<br>hello@tradecrest.com</span>
  </div>
  <div class="connect-btn">Connect ProNet</div>
</section>

<h2 class="section-title" style="top:3378px"><span class="p">Support</span></h2>
<p class="support-text">Have questions? Our dedicated support team is here to assist you.<br>Feel free to reach out to <u>hello@tradecrest.com</u> for personalised guidance.</p>

<div class="faq" style="top:3527px"><span>Doconsectetum ipsum adip?</span><svg width="14" height="9" viewBox="0 0 14 9"><path d="M1 1l6 6 6-6" fill="none" stroke="#8a0b8f" stroke-width="2"/></svg></div>
<div class="faq" style="top:3592px"><span>Doconsectetum ipsum adip?</span><svg width="14" height="9" viewBox="0 0 14 9"><path d="M1 1l6 6 6-6" fill="none" stroke="#8a0b8f" stroke-width="2"/></svg></div>
<div class="faq" style="top:3657px"><span>Wolor sit amet, consectetur adip?</span><svg width="14" height="9" viewBox="0 0 14 9"><path d="M1 1l6 6 6-6" fill="none" stroke="#8a0b8f" stroke-width="2"/></svg></div>
<div class="faq" style="top:3720px"><span>Doconsectetum ipsum adip?</span><svg width="14" height="9" viewBox="0 0 14 9"><path d="M1 1l6 6 6-6" fill="none" stroke="#8a0b8f" stroke-width="2"/></svg></div>
<div class="faq" style="top:3784px"><span>Doconsectetum ipsum adip?</span><svg width="14" height="9" viewBox="0 0 14 9"><path d="M1 1l6 6 6-6" fill="none" stroke="#8a0b8f" stroke-width="2"/></svg></div>
<div class="faq" style="top:3847px"><span>Lorem ipsum dolo consectetur adip?</span><svg width="14" height="9" viewBox="0 0 14 9"><path d="M1 1l6 6 6-6" fill="none" stroke="#8a0b8f" stroke-width="2"/></svg></div>

<footer class="footer">
  <div class="footer-band" role="img" aria-label="Decorative blue and purple wave band"></div>
  <div class="footer-brand"><i></i>TradeCrest</div>
  <nav class="footer-menu"><span>Home</span><span>About</span><span>Our Team</span><span>Key Features</span><span>Why Choose TradeCrest</span><span>Contact</span><span>Support</span><span>FAQ</span></nav>
  <p class="copyright">Copyright© 2023 TradeCrest. All Rights Reserved.</p>
  <div class="social" role="img" aria-label="Social profile link"></div>
  <div class="contact-us">Contact Us</div>
</footer>

</body>
</html>
```